Update shopping site

Our current shopping website is outdated and we are wanting to update our shopping site to have a fresh new look/design.

Create a Web Design (Uncoded - PSD layout only)

We want you to develop the design for 4 pages:
1) Home Page
2) Remedy Type
3) Health Condition
4) Consultations

www.fernmoorwell.com

Reason: Close to choosing design and a few missing items to be resolved.

Industry/Entity Type

Shopping

```html
<!DOCTYPE html>
<html lang="en">
<head>
<meta charset="UTF-8">
<title>Herb Catalogue</title>
<link href="https://fonts.googleapis.com/css2?family=Roboto:wght@400;500;700&display=swap" rel="stylesheet">
<style>
  :root {
    --page-bg: #f9f9f9;
    --green: #23a14b;
    --ink: #2e3d42;
    --text: #3a3f41;
    --white: #ffffff;
    --jar-top: #e4e4e4;
    --jar-mid: #cfd0c8;
    --jar-bottom: #efefef;
    --pile-white: #ffffff;
    --pile-tint: #c9d4c2;
  }
  * { margin: 0; padding: 0; box-sizing: border-box; }
  html, body {
    width: 1200px; height: 675px; overflow: hidden;
    background: var(--page-bg);
    font-family: 'Roboto', Arial, sans-serif;
  }
  .catalogue { position: relative; width: 1200px; height: 675px; }

  .btn {
    position: absolute;
    display: flex; align-items: center; justify-content: center;
    width: 105px; height: 36px; border-radius: 18px;
    font-size: 9.5px; font-weight: 700; letter-spacing: 1px;
    text-transform: uppercase; white-space: nowrap;
  }
  .btn-cart { background: var(--green); color: var(--white); }
  .btn-info { border: 2px solid var(--green); color: var(--green); background: transparent; }

  .product-photo { position: absolute; }
  .photo-jar {
    left: 227px; top: 116px; width: 264px; height: 329px;
    background: linear-gradient(180deg, var(--jar-top) 0%, var(--jar-mid) 55%, var(--jar-bottom) 100%);
  }
  .photo-pile {
    left: 709px; top: 150px; width: 265px; height: 249px;
    background: linear-gradient(180deg, var(--pile-white) 0%, var(--pile-tint) 50%, var(--pile-white) 100%);
  }

  .product-title {
    position: absolute;
    font-size: 17.5px; font-weight: 500; letter-spacing: 1.8px;
    color: var(--ink); text-transform: uppercase; white-space: nowrap;
  }
  .title-rule { position: absolute; width: 26px; height: 3px; background: var(--green); }
  .product-desc {
    position: absolute; width: 240px;
    font-size: 12px; font-weight: 500; line-height: 20px;
    letter-spacing: 0.2px; color: var(--text);
  }
  .product-desc.wide { width: 300px; white-space: nowrap; }
</style>
</head>
<body>
<main class="catalogue">

  <span class="btn btn-cart" style="left:227px; top:-23px;">Add to cart</span>
  <span class="btn btn-info" style="left:387px; top:-23px;">More info</span>

  <p class="product-desc wide" style="left:709px; top:-5px;">relieve irritations of the urinary tract.</p>
  <span class="btn btn-cart" style="left:709px; top:39px;">Add to cart</span>
  <span class="btn btn-info" style="left:868px; top:39px;">More info</span>

  <article class="product-card">
    <div class="product-photo photo-jar" role="img" aria-label="Photo of a glass jar filled with dried agrimony herb"></div>
    <h2 class="product-title" style="left:227px; top:462px;">Agrinomy Herb</h2>
    <div class="title-rule" style="left:227px; top:501px;"></div>
    <p class="product-desc" style="left:228px; top:519px;">Agrimony herb, cut &amp; sifted - Dried Herb (bulk) (Agrimonia eupatoria).</p>
    <span class="btn btn-cart" style="left:227px; top:584px;">Add to cart</span>
    <span class="btn btn-info" style="left:387px; top:584px;">More info</span>
  </article>

  <article class="product-card">
    <div class="product-photo photo-pile" role="img" aria-label="Photo of a pile of dried alfalfa herb on white"></div>
    <h2 class="product-title" style="left:711px; top:417px;">Alfalfa Herb</h2>
    <div class="title-rule" style="left:709px; top:455px;"></div>
    <p class="product-desc" style="left:709px; top:473px;">Alfalfa herb (Organic) - Dried Herb (bulk) (Medicago sativa).</p>
    <span class="btn btn-cart" style="left:709px; top:538px;">Add to cart</span>
    <span class="btn btn-info" style="left:868px; top:538px;">More info</span>
  </article>

  <span class="btn btn-info" style="left:549px; top:669px; width:101px;"></span>

</main>
</body>
</html>
```